Documentary Film Poster Design Project

I'm looking to hire someone to design a 11 x 17 poster for my documentary film, "Past the Shoal," which is about plastic pollution in the atlantic ocean. The film is accepted into four film international film festivals (so far), so your design would have wide exposure.

www.pasttheshoal-film.example

I'm looking for something fairly straightforward, that incorporates some textual information for the film, along with (maybe) existing photographs and your amazing design skills. Please do not include images of PET soda/water bottles. The film has a science advisory board which is very specific about using the correct representation of oceanic plastic pollution.

I'd like to own the rights to this poster and have the poster be scalable to printed postcards and DVD packaging.

Target Market(s)

This poster will be used at film festivals to promote the film and attract viewers to attend. It should be bold and striking, making people take notice of it and say, "that's a cool poster, I'd like to see that film about plastic pollution. It also looks like it was filmed on a ship. cool."

Industry/Entity Type

Plastic

Requirements
Must have
• The poster must have the following textual information in it. Basically as you see in any movie poster. I'm looking for interesting typography in this poster, especially with the title. In someway, I think it would be nice to play with the idea of little pieces of plastic in the visual look of the title, but that's for you to decide. I've also attached images of the motion-graphics in the film, but do not feel like you have to use these.

Past the Shoal

A documentary about plastic pollution

A 812reels production A film by Mark Dunbury
cinematography by Mark Dunbury and Lou Tarnowitzky edited by Mark Dunbury written by Mark Dunbury and Nora Dunbury produced and directed by Mark Dunbury

www.pasttheshoal-film.example
www.friendwall.example/PastTheShoalFilm

```html
<!DOCTYPE html>
<html lang="en">
<head>
<meta charset="utf-8">
<title>Past the Shoal — Poster</title>
<link rel="stylesheet" href="https://fonts.googleapis.com/css2?family=Anton&family=Roboto+Condensed:wght@400;700&display=swap">
<style>
  :root {
    --ocean-navy: #1c2657;
    --lavender: #c8b9ee;
    --periwinkle: #8ea2e6;
    --sage: #6f8a78;
    --leaf: #7db86a;
    --salmon: #dd9a7b;
    --khaki: #d8d39f;
    --deck-dark: #6e6357;
    --deck-light: #c3bbae;
    --white: #ffffff;
  }
  * { margin: 0; padding: 0; box-sizing: border-box; }
  html, body { width: 776px; height: 1200px; overflow: hidden; background: var(--white); }
  .poster {
    position: relative;
    width: 776px;
    height: 1200px;
    overflow: hidden;
    background: var(--ocean-navy);
    font-family: "Roboto Condensed", "Arial Narrow", sans-serif;
    color: var(--white);
  }
  .fragment-field {
    position: absolute;
    left: 0; top: 0;
    width: 776px; height: 978px;
    background:
      radial-gradient(circle at 20% 25%, rgba(125,184,106,.55), transparent 45%),
      radial-gradient(circle at 80% 40%, rgba(221,154,123,.5), transparent 45%),
      radial-gradient(circle at 30% 75%, rgba(142,162,230,.6), transparent 50%),
      radial-gradient(circle at 75% 85%, rgba(216,211,159,.5), transparent 45%),
      linear-gradient(160deg, var(--lavender), var(--sage) 50%, var(--periwinkle));
  }
  .title {
    position: absolute;
    left: 0; top: 0;
    width: 776px; height: 978px;
  }
  .title text {
    font-family: "Anton", "Impact", sans-serif;
    fill: var(--ocean-navy);
  }
  .deck-photo {
    position: absolute;
    left: 0; top: 978px;
    width: 776px; height: 222px;
    background: linear-gradient(180deg, var(--deck-light) 0%, #a39a8c 40%, var(--deck-dark) 100%);
  }
  .tagline {
    position: absolute;
    left: 160px; top: 1052px;
    font-size: 37px;
    font-weight: 700;
    letter-spacing: 0.2px;
    white-space: nowrap;
  }
  .credits {
    position: absolute;
    left: 88px; top: 1106px;
    width: 330px;
    font-size: 10px;
    line-height: 14px;
    font-weight: 400;
  }
  .links {
    position: absolute;
    right: 16px; top: 1117px;
    text-align: right;
    font-size: 10px;
    line-height: 15px;
    font-weight: 700;
    white-space: nowrap;
  }
</style>
</head>
<body>
  <main class="poster">
    <div class="fragment-field" role="img" aria-label="Mosaic of colourful rounded plastic fragments floating over dark ocean water, crossed by ship ropes"></div>

    <svg class="title" viewBox="0 0 776 978" aria-label="Past the Shoal">
      <text x="150" y="300" font-size="330" textLength="476" lengthAdjust="spacingAndGlyphs">PAST</text>
      <text x="175" y="610" font-size="330" textLength="430" lengthAdjust="spacingAndGlyphs">THE</text>
      <text x="150" y="915" font-size="330" textLength="480" lengthAdjust="spacingAndGlyphs">SHOAL</text>
    </svg>

    <div class="deck-photo" role="img" aria-label="Ship deck with rigging and cables seen from below"></div>

    <p class="tagline">A documentary about plastic pollution</p>

    <p class="credits">A 812reels production A film by Mark Dunbury. Edited by Mark Dunbury. Cinematography by Mark Dunbury and Lou Tarnowitzky. written by Mark Dunbury and Nora Dunbury produced and directed by Mark Dunbury.</p>

    <p class="links">www.pasttheshoal-film.example<br>www.friendwall.example/PastTheShoalFilm</p>
  </main>
</body>
</html>
```